Fresh pet feed direct from manufacturer to door step. Quality and Freshness un-surpassed in Industr

Need Business Card Design; leading into many other projects, for New Franchised Business Opportunity providing home delivery of fresh dog and cat feed (no emphasis needed for cat) direct from manufacturing facility. (no middle men or distributors) Food is Farm to Factory fresh. Our trademarked tagline is "Quality is our MAIN Ingredient ! "
Updates

Please take note of other contest for Chirplane Cover and Profile Pic's

Target Market(s)

Dog and Cat owners

Industry/Entity Type

Pet

Contact Information for Business Card

Name, address, local phone, national 800 number, website, email address

Other font styles liked:
• follow that from logo

Requirements
Must have
• Our feed is made in Texas with ingredients sourced from local farms. We want to lean heavy on the Made in West Texas , ranch theme but that has a 'black label', 'vantrel', 'premium', 'high-end' look and feel
Nice to have
• maybe have an offer on card? 20% off with promo code "x" etc.. ?? just a thought...

```html
<!DOCTYPE html>
<html lang="en">
<head>
<meta charset="utf-8">
<title>Hollin Ranch Premium – Business Card</title>
<link href="https://fonts.googleapis.com/css2?family=EB+Garamond:ital,wght@0,400;0,700;1,400&family=Open+Sans:ital,wght@0,400;0,700;1,400&display=swap" rel="stylesheet">
<style>
  :root {
    --backdrop: #e9e7e4;
    --card-white: #ffffff;
    --ink: #111111;
    --gold: #c9a23a;
    --gold-light: #f2d27a;
    --gold-dark: #8a6a1c;
    --paper-text: #1a1a1a;
    --on-black: #ffffff;
  }
  * { box-sizing: border-box; margin: 0; padding: 0; }
  html, body {
    width: 1200px; height: 768px; overflow: hidden;
    background: var(--backdrop);
  }
  .stage { position: relative; width: 1200px; height: 768px; }
  .card {
    position: absolute; top: 236px;
    width: 520px; height: 297px;
    background: var(--card-white);
    box-shadow: 0 6px 18px rgba(0,0,0,.18);
    overflow: hidden;
  }
  .card--front { left: 50px; }
  .card--back  { left: 630px; }

  .lockup {
    position: absolute;
    display: flex; flex-direction: column; gap: 12px;
  }
  .card--front .lockup {
    left: 0; right: 0; top: 112px;
    align-items: center;
  }
  .card--back .lockup {
    left: 40px; top: 58px;
    align-items: flex-start;
  }

  .brand {
    font-family: "EB Garamond", serif;
    font-weight: 700;
    color: var(--ink);
    letter-spacing: 1px;
    display: flex; align-items: center; gap: 10px;
    white-space: nowrap;
  }
  .brand__dot {
    width: 12px; height: 12px; border-radius: 50%;
    background: var(--gold); flex: none;
  }
  .brand__name { font-size: 26px; line-height: 1; text-transform: uppercase; }

  .tagline {
    font-family: "EB Garamond", serif;
    font-size: 15px; line-height: 1.2;
    color: var(--paper-text);
    white-space: nowrap;
  }

  .card__art { position: absolute; inset: 0; }

  .person {
    position: absolute; right: 34px; top: 112px; text-align: right;
    font-family: "Open Sans", sans-serif;
  }
  .person__name { color: var(--gold); font-weight: 700; font-size: 17px; }
  .person__title { color: var(--ink); font-style: italic; font-size: 15px; margin-top: 2px; }

  .contacts {
    position: absolute; right: 22px; top: 210px;
    list-style: none;
    font-family: "Open Sans", sans-serif;
    font-size: 13.5px; color: var(--on-black);
  }
  .contacts li {
    display: flex; justify-content: flex-end; align-items: center;
    gap: 10px; height: 20px; white-space: nowrap;
  }
  .contacts svg { width: 14px; height: 14px; fill: var(--gold); flex: none; }
</style>
</head>
<body>
<main class="stage">

  <section class="card card--front" aria-label="Card front">
    <div class="lockup">
      <div class="brand">
        <span class="brand__dot"></span>
        <span class="brand__name">Hollin Ranch Premium</span>
      </div>
      <p class="tagline">Quality is our MAIN Ingredient !</p>
    </div>
  </section>

  <section class="card card--back" aria-label="Card back">
    <svg class="card__art" viewBox="0 0 520 297" preserveAspectRatio="none" aria-hidden="true">
      <defs>
        <linearGradient id="goldSweep" x1="0" x2="1" y1="0" y2="0">
          <stop offset="0" stop-color="var(--gold-dark)"/>
          <stop offset=".45" stop-color="var(--gold-light)"/>
          <stop offset=".75" stop-color="var(--gold)"/>
          <stop offset="1" stop-color="var(--gold-dark)"/>
        </linearGradient>
      </defs>
      <path d="M0,150 C140,205 300,222 520,205 L520,297 L0,297 Z" fill="var(--ink)"/>
      <path d="M40,150 C170,205 320,215 520,196" fill="none" stroke="url(#goldSweep)" stroke-width="7" stroke-linecap="round"/>
      <path d="M60,142 C190,192 330,204 520,186" fill="none" stroke="url(#goldSweep)" stroke-width="2"/>
    </svg>

    <div class="lockup">
      <div class="brand">
        <span class="brand__dot"></span>
        <span class="brand__name">Hollin Ranch Premium</span>
      </div>
      <p class="tagline">Quality is our MAIN Ingredient !</p>
    </div>

    <div class="person">
      <p class="person__name">Your Name</p>
      <p class="person__title">Your title</p>
    </div>

    <ul class="contacts">
      <li>00.00.00.0000
        <svg viewBox="0 0 16 16"><path d="M3 1h3l1 4-2 1c1 2 3 4 5 5l1-2 4 1v3c0 1-1 2-2 2C7 15 1 9 1 3c0-1 1-2 2-2z"/></svg>
      </li>
      <li>1800-123-123-123
        <svg viewBox="0 0 16 16"><path d="M8 0a5 5 0 0 1 5 5c0 4-5 11-5 11S3 9 3 5a5 5 0 0 1 5-5zm0 3a2 2 0 1 0 0 4 2 2 0 0 0 0-4z"/></svg>
      </li>
      <li>www.yourwebsite.com
        <svg viewBox="0 0 16 16"><path d="M8 0a8 8 0 1 0 0 16A8 8 0 0 0 8 0zm0 1.5c1 1 1.8 3 2 5.5H6c.2-2.5 1-4.5 2-5.5zM1.6 7h3c.1-2 .7-3.8 1.5-5A6.5 6.5 0 0 0 1.6 7zm9.8 0h3A6.5 6.5 0 0 0 9.9 2c.8 1.2 1.4 3 1.5 5zM1.6 9a6.5 6.5 0 0 0 4.5 5c-.8-1.2-1.4-3-1.5-5zm4.4 0c.2 2.5 1 4.5 2 5.5 1-1 1.8-3 2-5.5zm5.4 0c-.1 2-.7 3.8-1.5 5a6.5 6.5 0 0 0 4.5-5z"/></svg>
      </li>
      <li>yourname@yourwebsite.com
        <svg viewBox="0 0 16 16"><path d="M0 3h16v10H0zM1.5 4.5 8 9l6.5-4.5V4h-13z"/></svg>
      </li>
    </ul>
  </section>

</main>
</body>
</html>
```